Contemporary restaurant add that stands out

I would like an ad that I can use for flyers and in guide books for a tourist restaurant. It must reflect high quality, be contemporary and stand out amongst other adverts.

The ad must try and say good quality food in pleasant surroundings.

The ad must be left open because different guide books require different size ads, so it must be able to resize.

I have included our current ad. I want it changed because some feedback I received say it looks more like a nightclub than a restaurant.

I also have more pics if necessary. Also I have pics of the restaurant in different colours

Target Market(s)

Tourists of various nationalities

Industry/Entity Type

Restaurant

Requirements
Must have
• The name of the restaurant is
• Paper Kite
• And it is in Edwardian script font with bold and italic selected.
• The ad must contain our phone number, address and free wifi. The details are on our current ad which is included

```html
<!DOCTYPE html>
<html lang="en">
<head>
<meta charset="utf-8">
<title>Paper Kite Restaurant Flyer</title>
<link rel="stylesheet" href="https://fonts.googleapis.com/css2?family=Great+Vibes&family=Montserrat:wght@400;600;700&display=swap">
<style>
  :root {
    --magenta: #c41fb4;
    --magenta-light: #e45ad8;
    --magenta-deep: #8e0f86;
    --panel: #121114;
    --grey-ring: #8a8a8f;
    --white: #ffffff;
    --url-ink: #1d1a20;
  }
  * { margin: 0; padding: 0; box-sizing: border-box; }
  html, body { width: 900px; height: 1200px; overflow: hidden; background: var(--panel); }
  .flyer {
    position: relative; width: 900px; height: 1200px; overflow: hidden;
    background: var(--panel);
    font-family: "Montserrat", Arial, sans-serif; color: var(--white);
  }
  .masthead {
    position: absolute; top: 0; left: 0; width: 900px; height: 200px;
    background: linear-gradient(180deg, var(--magenta-light) 0%, var(--magenta) 55%, var(--magenta-deep) 100%);
    text-align: center; z-index: 2;
  }
  .masthead__label {
    position: absolute; top: 18px; width: 100%;
    font-weight: 700; font-size: 32px; letter-spacing: 5px; line-height: 1;
  }
  .masthead__name {
    position: absolute; top: 62px; width: 100%;
    font-family: "Great Vibes", cursive; font-size: 112px; line-height: 1;
    font-weight: 400;
  }
  .venue-photo {
    position: absolute; top: 200px; left: 0; width: 900px; height: 360px;
    background:
      radial-gradient(ellipse 40% 30% at 50% 55%, rgba(255,170,90,0.45) 0%, rgba(255,170,90,0) 100%),
      linear-gradient(180deg, #1e0a2a 0%, #5a1a6e 30%, #b232b4 55%, #e06adc 66%, #4a1650 84%, #160a18 100%);
  }
  .decor { position: absolute; left: 0; width: 900px; }
  .decor--mid { top: 480px; height: 130px; }
  .decor--foot { top: 1040px; height: 80px; }
  .speciality {
    position: absolute; top: 580px; left: 0; width: 100%;
    display: flex; justify-content: center; align-items: center; gap: 10px;
  }
  .speciality__dot { width: 30px; height: 30px; border-radius: 50%; border: 2px solid var(--magenta); }
  .speciality__text { font-family: "Great Vibes", cursive; font-size: 34px; line-height: 1; }
  .dish {
    position: absolute; border-radius: 50%;
    border: 10px solid var(--grey-ring);
    box-shadow: 0 0 0 6px var(--magenta), 0 0 0 9px #2b2a2e;
  }
  .dish--lamb { left: 100px; top: 680px; width: 200px; height: 200px;
    background: radial-gradient(circle at 45% 45%, #d9a070 0%, #8a5232 50%, #3a241a 100%); }
  .dish--grill { left: 330px; top: 650px; width: 240px; height: 240px;
    background: radial-gradient(circle, #f0962e 0%, #b8401c 45%, #3a140a 100%); }
  .dish--fish { left: 600px; top: 680px; width: 200px; height: 200px;
    background: radial-gradient(circle, #f6f2ea 0%, #ddd2b8 55%, #8a7a5a 100%); }
  .contact { position: absolute; top: 905px; width: 100%; text-align: center; }
  .contact__wifi-icon { display: block; margin: 0 auto 4px; }
  .contact__wifi { font-weight: 600; font-size: 24px; letter-spacing: 1px; line-height: 1.2; }
  .contact__label { font-weight: 600; font-size: 19px; margin-top: 4px; line-height: 1.2; }
  .contact__phone {
    margin-top: 6px; display: flex; justify-content: center; align-items: center; gap: 10px;
    color: var(--magenta-light); font-weight: 700; font-size: 22px;
  }
  .contact__address { margin-top: 12px; font-size: 14px; }
  .web-bar {
    position: absolute; top: 1110px; left: 0; width: 900px; height: 50px;
    background: var(--white); color: var(--url-ink);
    display: flex; align-items: center; justify-content: center;
    font-weight: 700; font-size: 28px; letter-spacing: 1px;
  }
  .foot-strip { position: absolute; top: 1160px; left: 0; width: 900px; height: 40px; background: var(--magenta); }
</style>
</head>
<body>
<div class="flyer">
  <header class="masthead">
    <div class="masthead__label">RESTAURANT</div>
    <h1 class="masthead__name">Paper Kite</h1>
  </header>

  <div class="venue-photo" role="img" aria-label="Evening view of the restaurant terrace lit in purple and pink"></div>

  <svg class="decor decor--mid" viewBox="0 0 900 130" aria-hidden="true">
    <path d="M0 130 L0 60 Q450 -10 900 60 L900 130 Z" fill="#121114"/>
    <path d="M0 60 Q450 -10 900 60" fill="none" stroke="#c41fb4" stroke-width="8"/>
    <path d="M0 78 Q450 10 900 78" fill="none" stroke="#e45ad8" stroke-width="2"/>
  </svg>

  <div class="speciality">
    <span class="speciality__dot"></span>
    <span class="speciality__text">Our Speciality</span>
  </div>

  <div class="dish dish--lamb" role="img" aria-label="Rack of lamb on a board"></div>
  <div class="dish dish--grill" role="img" aria-label="Steak on a flaming grill"></div>
  <div class="dish dish--fish" role="img" aria-label="Fish fillet with potatoes and sauce"></div>

  <section class="contact">
    <svg class="contact__wifi-icon" width="28" height="20" viewBox="0 0 30 22" aria-hidden="true">
      <path d="M2 8 Q15 -3 28 8" fill="none" stroke="#fff" stroke-width="2.5" stroke-linecap="round"/>
      <path d="M7 13 Q15 6 23 13" fill="none" stroke="#fff" stroke-width="2.5" stroke-linecap="round"/>
      <circle cx="15" cy="19" r="2.5" fill="#fff"/>
    </svg>
    <div class="contact__wifi">FREE WIFI</div>
    <div class="contact__label">FOR RESERVATIONS CONTACT:</div>
    <div class="contact__phone">
      <svg width="20" height="20" viewBox="0 0 24 24" aria-hidden="true">
        <circle cx="12" cy="12" r="11" fill="none" stroke="#fff" stroke-width="1.5"/>
        <path d="M8 6 L10 6 L11 9 L9.5 10.5 Q11 13.5 13.5 14.5 L15 13 L18 14 L18 16 Q17 18 15 18 Q8 17 6 9 Q6 7 8 6 Z" fill="#fff"/>
      </svg>
      <span>922481536</span>
    </div>
    <div class="contact__address">Paseo del Faro, C.C. Marina Azul, Playa Serena Los Alisios</div>
  </section>

  <svg class="decor decor--foot" viewBox="0 0 900 80" aria-hidden="true">
    <path d="M0 10 Q450 70 900 10 L900 80 L0 80 Z" fill="#c41fb4"/>
    <path d="M0 24 Q450 84 900 24" fill="none" stroke="#e45ad8" stroke-width="3"/>
    <path d="M0 0 Q450 58 900 0" fill="none" stroke="#8e0f86" stroke-width="4"/>
  </svg>

  <div class="web-bar">www.paperkite-restaurant.com</div>
  <div class="foot-strip"></div>
</div>
</body>
</html>
```